KORBLE Development is an idea development firm. This business card is for Weekend Wicket League, a site that allows users from all over the world to play fantasy cricket against each other.
We need a business card for WWL using our logo and its associated colors. The cards are for the two founders, Tobias Whitlow and Martin Dobrescu. We would like our own cards.
We are handing our card to potential investors and sponsors of our site. It needs to be unique (like our brand.)
Updates
I wanted to thank everyone for their awesome designs!!! It was a hard choice - we narrowed it down to 7 then to three then to 1. All of you are extremely talented - THANK YOU.
Target Market(s)
Potential Investors, Partners
Industry/Entity Type
Business
Contact Information for Business Card
Korble Development : Weekend Wicket League
Tobias Whitlow
Founder
555-204-7316
tobias@korble.example
www.weekendwicketleague.example
....
Martin Dobrescu
Founder
555-871-0492
martin@korble.example
Look and feel

```html
<!DOCTYPE html>
<html lang="en">
<head>
<meta charset="utf-8">
<title>Weekend Wicket League — Business Cards</title>
<link rel="stylesheet" href="https://fonts.googleapis.com/css2?family=Open+Sans:wght@400;600;700&display=swap">
<style>
  :root {
    --bg: #e6e6e3;
    --green-dark: #3e960f;
    --green-light: #7dc21c;
    --green-accent: #9be12a;
    --black: #0b0b0b;
    --white: #ffffff;
  }
  * { box-sizing: border-box; margin: 0; padding: 0; }
  html, body { width: 1200px; height: 900px; overflow: hidden; }
  body {
    position: relative;
    background: var(--bg);
    font-family: "Open Sans", Arial, sans-serif;
    color: var(--white);
  }
  .card {
    position: absolute;
    width: 520px;
    height: 297px;
    background: linear-gradient(180deg, var(--green-dark) 0%, var(--green-light) 100%);
    box-shadow: 0 8px 24px rgba(0,0,0,.25);
    overflow: hidden;
  }
  .card--front { left: 340px; top: 60px; }
  .card--tobias { left: 40px; top: 470px; }
  .card--martin { left: 640px; top: 470px; }

  .brand { display: flex; align-items: center; gap: 12px; }
  .brand__mark {
    width: 54px; height: 54px; border-radius: 50%;
    background: var(--white); flex: none;
  }
  .brand__name { font-weight: 600; font-size: 25px; color: var(--white); line-height: 1.1; }
  .brand__tagline { font-weight: 600; font-size: 11px; color: var(--white); margin-top: 3px; }

  .card--front .brand { position: absolute; left: 60px; top: 72px; }
  .front__band {
    position: absolute; left: 0; right: 0; top: 208px; height: 58px;
    background: var(--black);
    display: flex; align-items: center; justify-content: center;
    font-size: 19px; font-weight: 600; letter-spacing: .2px;
  }

  .contact {
    position: absolute; left: 24px; top: 22px; width: 200px; height: 253px;
    background: var(--black);
    padding: 20px 16px 0 18px;
  }
  .contact__firm { font-size: 14px; font-weight: 600; line-height: 1.15; }
  .contact__project { font-size: 14px; font-weight: 600; color: var(--green-accent); line-height: 1.15; }
  .contact__name { margin-top: 22px; font-size: 16px; font-weight: 700; color: var(--green-accent); text-transform: uppercase; text-align: center; }
  .contact__role { font-size: 16px; font-weight: 700; text-transform: uppercase; text-align: center; }
  .contact__list { list-style: none; margin-top: 26px; }
  .contact__item { display: flex; align-items: center; gap: 10px; font-size: 13px; font-weight: 600; margin-bottom: 10px; white-space: nowrap; }
  .contact__icon { width: 22px; height: 22px; flex: none; }

  .card--back .brand { position: absolute; left: 240px; top: 112px; gap: 8px; }
  .card--back .brand__mark { width: 40px; height: 40px; }
  .card--back .brand__name { font-size: 17px; }
  .card--back .brand__tagline { font-size: 8px; }
</style>
</head>
<body>

  <section class="card card--front" aria-label="Card front">
    <div class="brand">
      <span class="brand__mark"></span>
      <div>
        <div class="brand__name">Weekend Wicket League</div>
        <div class="brand__tagline">The World's Premier Fantasy Cricket Game</div>
      </div>
    </div>
    <div class="front__band">www.weekendwicketleague.example</div>
  </section>

  <section class="card card--back card--tobias" aria-label="Card back, Tobias Whitlow">
    <div class="contact">
      <div class="contact__firm">KORBLE Development:</div>
      <div class="contact__project">Weekend Wicket League</div>
      <div class="contact__name">Tobias Whitlow</div>
      <div class="contact__role">Founder</div>
      <ul class="contact__list">
        <li class="contact__item">
          <svg class="contact__icon" viewBox="0 0 22 22" aria-hidden="true"><circle cx="11" cy="11" r="11" fill="#fff"/><path d="M6 8.5c0-1.5 2.5-2.5 5-2.5s5 1 5 2.5v1h-2.5v-1h-5v1H6z M7.5 11h7l1 4.5h-9z" fill="#0b0b0b"/><circle cx="11" cy="13" r="1.3" fill="#fff"/></svg>
          555-204-7316
        </li>
        <li class="contact__item">
          <svg class="contact__icon" viewBox="0 0 22 22" aria-hidden="true"><circle cx="11" cy="11" r="11" fill="#fff"/><rect x="5.5" y="7" width="11" height="8" fill="#0b0b0b"/><path d="M5.5 7l5.5 4.5L16.5 7" fill="none" stroke="#fff" stroke-width="1"/></svg>
          tobias@korble.example
        </li>
      </ul>
    </div>
    <div class="brand">
      <span class="brand__mark"></span>
      <div>
        <div class="brand__name">Weekend Wicket League</div>
        <div class="brand__tagline">The World's Premier Fantasy Cricket Game</div>
      </div>
    </div>
  </section>

  <section class="card card--back card--martin" aria-label="Card back, Martin Dobrescu">
    <div class="contact">
      <div class="contact__firm">KORBLE Development:</div>
      <div class="contact__project">Weekend Wicket League</div>
      <div class="contact__name">Martin Dobrescu</div>
      <div class="contact__role">Founder</div>
      <ul class="contact__list">
        <li class="contact__item">
          <svg class="contact__icon" viewBox="0 0 22 22" aria-hidden="true"><circle cx="11" cy="11" r="11" fill="#fff"/><path d="M6 8.5c0-1.5 2.5-2.5 5-2.5s5 1 5 2.5v1h-2.5v-1h-5v1H6z M7.5 11h7l1 4.5h-9z" fill="#0b0b0b"/><circle cx="11" cy="13" r="1.3" fill="#fff"/></svg>
          555-871-0492
        </li>
        <li class="contact__item">
          <svg class="contact__icon" viewBox="0 0 22 22" aria-hidden="true"><circle cx="11" cy="11" r="11" fill="#fff"/><rect x="5.5" y="7" width="11" height="8" fill="#0b0b0b"/><path d="M5.5 7l5.5 4.5L16.5 7" fill="none" stroke="#fff" stroke-width="1"/></svg>
          martin@korble.example
        </li>
      </ul>
    </div>
    <div class="brand">
      <span class="brand__mark"></span>
      <div>
        <div class="brand__name">Weekend Wicket League</div>
        <div class="brand__tagline">The World's Premier Fantasy Cricket Game</div>
      </div>
    </div>
  </section>

</body>
</html>
```